Business Card Trevian Digital

Design of two business cards (board) for Trevian Digital. Trevian Digital DMCC, based in in Dubai U.A.E. Trevian Digital is a self-contained online company, taking an online concept from idea to reality. Concretely, this has involved the (partly remote) management, website development, market implementation and mobile application development for several platforms.

Frontside of business card should feature our company logo (Trevian) and personal details. Backside should feature the logo's of our current brands (mendquickly, taskpalace and galaplanner). We would prefer a design based on the grey/orange color scheme of our company. Trevian Digital is a young, modern and dynamic company and we would like to see this reflected in the design.

```html
<!DOCTYPE html>
<html lang="en">
<head>
<meta charset="utf-8">
<title>Trevian Digital – Business Card</title>
<link rel="stylesheet" href="https://fonts.googleapis.com/css2?family=Jura:wght@500;600;700&display=swap">
<style>
  :root {
    --backdrop: #d9d6d2;
    --card-light: #e9e9e9;
    --card-white: #f1f1f1;
    --slate: #5d5d5d;
    --slate-edge: #d2d2d2;
    --orange: #ee6436;
    --ink-light: #ffffff;
    --mark-grey: #5d5d5d;
  }
  * { margin: 0; padding: 0; box-sizing: border-box; }
  html, body {
    width: 1200px; height: 800px; overflow: hidden;
    background: var(--backdrop);
    font-family: "Jura", "Segoe UI", sans-serif;
  }
  .board {
    position: relative; width: 1200px; height: 800px;
    display: flex; flex-direction: column; align-items: center; justify-content: center; gap: 40px;
  }
  .card {
    position: relative; width: 580px; height: 340px; overflow: hidden;
    box-shadow: 0 6px 18px rgba(0,0,0,0.18);
  }
  .card-front { background: var(--card-light); }
  .card-back { background: var(--card-white); }
  .card-shapes { position: absolute; inset: 0; }

  .brand { position: absolute; display: flex; flex-direction: column; align-items: center; }
  .brand-dot { width: 84px; height: 84px; border-radius: 50%; background: var(--mark-grey); }
  .brand-name {
    margin-top: 22px; color: var(--orange); font-weight: 500;
    font-size: 26px; letter-spacing: 6px;
  }
  .card-front .brand { left: 38px; top: 78px; width: 170px; }
  .card-back .brand { left: 0; right: 0; top: 56px; }
  .card-back .brand-dot { width: 64px; height: 64px; }
  .card-back .brand-name { font-size: 22px; margin-top: 18px; }

  .brand-band {
    position: absolute; left: 0; right: 0; bottom: 0; height: 96px;
    background: var(--slate);
    border-top: 6px solid var(--orange);
    display: flex; align-items: center; justify-content: space-evenly;
  }
  .sub-brand { display: flex; align-items: center; gap: 8px; }
  .sub-brand-dot { width: 14px; height: 14px; border-radius: 50%; background: var(--orange); }
  .sub-brand-name {
    color: var(--ink-light); font-weight: 600; font-size: 17px; letter-spacing: 1px;
  }

  .details { position: absolute; right: 22px; color: var(--ink-light); text-align: right; }
  .person { top: 26px; }
  .person-name { font-size: 20px; font-weight: 600; letter-spacing: 1px; }
  .person-role { font-size: 12px; font-weight: 600; letter-spacing: 1px; margin-top: 2px; }
  .address { top: 120px; font-size: 15px; font-weight: 600; line-height: 21px; right: 30px; }
  .contacts { top: 210px; font-size: 13px; font-weight: 600; }
  .contact-line { display: flex; align-items: center; justify-content: flex-end; gap: 10px; height: 21px; }
  .contact-line.small { font-size: 11.5px; }
  .contact-icon { width: 14px; height: 14px; flex: none; }
</style>
</head>
<body>
<main class="board">

  <section class="card card-front" aria-label="Business card front">
    <svg class="card-shapes" viewBox="0 0 580 340" width="580" height="340" aria-hidden="true">
      <path d="M215 0 L580 0 L580 340 L150 340 C240 285 300 190 290 110 C284 65 262 28 238 0 Z" fill="var(--slate-edge)"/>
      <path d="M232 0 L580 0 L580 340 L166 340 C252 285 312 190 302 110 C296 65 276 28 254 0 Z" fill="var(--slate)"/>
      <path d="M196 0 L254 0 C282 40 300 90 302 140 C303 170 297 195 288 215 C292 160 276 100 244 52 C230 32 214 14 196 0 Z" fill="var(--orange)"/>
    </svg>

    <div class="brand">
      <div class="brand-dot"></div>
      <div class="brand-name">TREVIAN</div>
    </div>

    <div class="details person">
      <div class="person-name">DORIAN KESWICK</div>
      <div class="person-role">FINANCIAL ADVISOR</div>
    </div>

    <div class="details address">
      <div>047.12th floor,Arc</div>
      <div>Meridian Road DXB</div>
    </div>

    <div class="details contacts">
      <div class="contact-line">012 555 0142
        <svg class="contact-icon" viewBox="0 0 14 14"><path d="M3 1 L5 1 L6 4 L4.5 5.2 C5.3 7 6.9 8.7 8.8 9.5 L10 8 L13 9 L13 11 C13 12 12 13 11 13 C5.5 12.5 1.5 8.5 1 3 C1 2 2 1 3 1 Z" fill="var(--ink-light)"/></svg>
      </div>
      <div class="contact-line">012 555 0187
        <svg class="contact-icon" viewBox="0 0 14 14"><rect x="3.5" y="0.8" width="7" height="12.4" rx="1.3" fill="none" stroke="var(--ink-light)" stroke-width="1.3"/><circle cx="7" cy="11" r="0.8" fill="var(--ink-light)"/></svg>
      </div>
      <div class="contact-line">012 555 0163
        <svg class="contact-icon" viewBox="0 0 14 14"><rect x="1" y="5" width="12" height="8" rx="1" fill="var(--ink-light)"/><rect x="3.5" y="1" width="7" height="5" fill="var(--ink-light)"/><rect x="3" y="8" width="8" height="1.2" fill="var(--slate)"/><rect x="3" y="10" width="8" height="1.2" fill="var(--slate)"/></svg>
      </div>
      <div class="contact-line small">dkeswick@mailbox.com
        <svg class="contact-icon" viewBox="0 0 14 14"><rect x="1" y="3" width="12" height="8.5" fill="var(--ink-light)"/><path d="M1.5 3.5 L7 8 L12.5 3.5" fill="none" stroke="var(--slate)" stroke-width="1.1"/></svg>
      </div>
      <div class="contact-line small">www.treviandigital.com
        <svg class="contact-icon" viewBox="0 0 14 14"><g fill="none" stroke="var(--ink-light)" stroke-width="1.1"><circle cx="7" cy="7" r="5.8"/><ellipse cx="7" cy="7" rx="2.5" ry="5.8"/><path d="M1.2 7 H12.8 M2.2 4 H11.8 M2.2 10 H11.8"/></g></svg>
      </div>
    </div>
  </section>

  <section class="card card-back" aria-label="Business card back">
    <div class="brand">
      <div class="brand-dot"></div>
      <div class="brand-name">TREVIAN</div>
    </div>

    <div class="brand-band">
      <div class="sub-brand"><span class="sub-brand-dot"></span><span class="sub-brand-name">mendquickly</span></div>
      <div class="sub-brand"><span class="sub-brand-dot"></span><span class="sub-brand-name">taskpalace</span></div>
      <div class="sub-brand"><span class="sub-brand-dot"></span><span class="sub-brand-name">galaplanner</span></div>
    </div>
  </section>

</main>
</body>
</html>
```